Brenmor Water - 500ml

to create a water bottle packaging similar to Brume Claire design. Bottle should be blue similar to NORTH KIND but change the design/logo to Brenmor. Wording should be similar just different design and logo. Thanks.

Colors
0054AA
0677BA
7BADD7
CADEEF
E8F1F8

Requirements
Must have
• Bottle must not be in plastic bottles. They are made in a carton instead - see NORTH KIND for reference.

```html
<!DOCTYPE html>
<html lang="en">
<head>
<meta charset="utf-8">
<title>Brenmor Water 500 ml carton front</title>
<link href="https://fonts.googleapis.com/css2?family=Oswald:wght@500;600&family=Open+Sans:wght@400;700&display=swap" rel="stylesheet">
<style>
  :root {
    --navy: #0054AA;
    --ocean: #0677BA;
    --sky: #7BADD7;
    --mist: #CADEEF;
    --foam: #E8F1F8;
    --white: #FFFFFF;
  }
  html, body {
    margin: 0;
    padding: 0;
    width: 843px;
    height: 1200px;
    overflow: hidden;
    background: var(--white);
  }
  .carton-front {
    position: relative;
    width: 843px;
    height: 1200px;
    overflow: hidden;
  }
  .facet-backdrop {
    position: absolute;
    inset: 0;
    width: 100%;
    height: 100%;
  }
  .brand-block {
    position: absolute;
    top: 345px;
    left: 0;
    width: 100%;
    text-align: center;
  }
  .brand-name {
    font-family: "Oswald", sans-serif;
    font-weight: 600;
    font-size: 112px;
    line-height: 1;
    color: var(--navy);
    margin: 0;
  }
  .brand-tagline {
    font-family: "Open Sans", sans-serif;
    font-weight: 700;
    font-size: 15px;
    letter-spacing: 2px;
    color: var(--navy);
    margin: 10px 0 0;
  }
  .product-name {
    position: absolute;
    top: 500px;
    left: 0;
    width: 100%;
    text-align: center;
    font-family: "Oswald", sans-serif;
    font-weight: 500;
    font-size: 150px;
    line-height: 1;
    letter-spacing: 4px;
    color: var(--navy);
    margin: 0;
  }
  .claims {
    position: absolute;
    top: 850px;
    left: 0;
    width: 100%;
    text-align: center;
    color: var(--white);
    font-family: "Open Sans", sans-serif;
  }
  .claims-headline {
    font-weight: 700;
    font-size: 40px;
    margin: 0 0 14px;
  }
  .claims-detail {
    font-weight: 400;
    font-size: 28px;
    line-height: 1.35;
    margin: 0;
  }
  .volume {
    position: absolute;
    top: 1010px;
    left: 0;
    width: 100%;
    text-align: center;
    font-family: "Oswald", sans-serif;
    font-weight: 500;
    font-size: 42px;
    letter-spacing: 1px;
    color: var(--white);
    margin: 0;
  }
</style>
</head>
<body>
  <main class="carton-front">
    <svg class="facet-backdrop" viewBox="0 0 843 1200" preserveAspectRatio="none" role="img" aria-label="Soft faceted low-poly pattern fading from white at the top to deep blue at the bottom">
      <defs>
        <linearGradient id="water-fade" x1="0" y1="0" x2="0" y2="1">
          <stop offset="0" stop-color="#FFFFFF"/>
          <stop offset="0.22" stop-color="#E8F1F8"/>
          <stop offset="0.45" stop-color="#CADEEF"/>
          <stop offset="0.65" stop-color="#7BADD7"/>
          <stop offset="0.85" stop-color="#0677BA"/>
          <stop offset="1" stop-color="#0054AA"/>
        </linearGradient>
      </defs>
      <rect x="0" y="0" width="843" height="1200" fill="url(#water-fade)"/>
    </svg>

    <section class="brand-block">
      <p class="brand-name">Brenmor</p>
      <p class="brand-tagline">PURE SOURCE | EST. 1998</p>
    </section>

    <h1 class="product-name">WATER</h1>

    <section class="claims">
      <p class="claims-headline">100% Spring Water</p>
      <p class="claims-detail">Sustainably sourced water<br>in a plant-based carton</p>
    </section>

    <p class="volume">500 ML</p>
  </main>
</body>
</html>
```